Visitenkarten für ein Metallverarbeitsungsbetrieb
Zielgruppe
Metallverarbeitsungsbetrieb
spezialisiert auf Lasern
Aufgabenstellung
Passend zu unseren Logo und in den Farben, schlicht dennoch besonders

```html
<!DOCTYPE html>
<html lang="de">
<head>
<meta charset="utf-8">
<title>Visitenkarte – Nordhelm Laser GmbH</title>
<link rel="stylesheet" href="https://fonts.googleapis.com/css2?family=Barlow+Condensed:wght@400;500&display=swap">
<style>
  :root {
    --backdrop: #e8ecef;
    --card: #ffffff;
    --brand-blue: #0a7bb0;
    --text-grey: #666666;
  }
  * { margin: 0; padding: 0; box-sizing: border-box; }
  html, body {
    width: 1200px;
    height: 1200px;
    overflow: hidden;
    background: var(--backdrop);
    font-family: "Barlow Condensed", "Arial Narrow", sans-serif;
  }
  .canvas { position: relative; width: 1200px; height: 1200px; }
  .card {
    position: absolute;
    left: 255px;
    width: 776px;
    height: 444px;
    background: var(--card);
  }
  .card--front { top: 141px; }
  .card--back { top: 615px; }

  .brand {
    position: absolute;
    display: flex;
    align-items: center;
    color: var(--brand-blue);
    font-weight: 500;
    white-space: nowrap;
  }
  .brand__square { background: var(--brand-blue); flex: none; }
  .card--front .brand { left: 101px; top: 198px; font-size: 46px; gap: 18px; }
  .card--front .brand__square { width: 56px; height: 56px; }
  .card--back .brand { left: 440px; top: 276px; font-size: 30px; gap: 12px; }
  .card--back .brand__square { width: 36px; height: 36px; }

  .person { position: absolute; left: 76px; top: 76px; }
  .person__name {
    color: var(--brand-blue);
    font-size: 40px;
    font-weight: 400;
    line-height: 1;
  }
  .person__role {
    margin-top: 12px;
    color: var(--text-grey);
    font-size: 25px;
    line-height: 1;
  }
  .contact {
    position: absolute;
    left: 81px;
    top: 222px;
    color: var(--text-grey);
    font-size: 25px;
    line-height: 34px;
  }
  .contact__web { margin-top: 14px; letter-spacing: 2px; }
</style>
</head>
<body>
<div class="canvas">
  <section class="card card--front">
    <div class="brand"><span class="brand__square"></span>Nordhelm Laser GmbH</div>
  </section>

  <section class="card card--back">
    <div class="person">
      <h1 class="person__name">YOUR NAME</h1>
      <p class="person__role">Owner/President</p>
    </div>
    <div class="contact">
      <p>City name, Your Country</p>
      <p>P:&nbsp; (123) 456789</p>
      <div class="contact__web">
        <p>name@yourcompany.de</p>
        <p>www.yourcompany.com</p>
      </div>
    </div>
    <div class="brand"><span class="brand__square"></span>Nordhelm Laser GmbH</div>
  </section>
</div>
</body>
</html>
```